Velmarine - Mechanic/Collision Center Business Card

We're looking for a business card design for our mechanic/ collision repair shop.

Can be with colours or monochromatic.

See the attached files.

Many thanks

```html
<!DOCTYPE html>
<html lang="pt">
<head>
<meta charset="utf-8">
<title>Velmarine – Business Card</title>
<link href="https://fonts.googleapis.com/css2?family=Arimo:wght@400;700&display=swap" rel="stylesheet">
<style>
  :root {
    --backdrop: #dadcdb;
    --ink: #292827;
    --paper: #ffffff;
  }
  * { margin: 0; padding: 0; box-sizing: border-box; }
  html, body {
    width: 1200px; height: 1200px; overflow: hidden;
    background: var(--backdrop);
    font-family: "Arimo", Arial, sans-serif;
  }
  .canvas { position: relative; width: 1200px; height: 1200px; }
  .card { position: absolute; overflow: hidden; }
  .card--front { left: 202px; top: 96px; width: 828px; height: 460px; background: var(--paper); color: var(--ink); }
  .card--back { left: 200px; top: 620px; width: 828px; height: 460px; background: var(--ink); color: var(--paper); }

  .block { position: absolute; }
  /* front card brand block */
  .front-brand { left: 0; top: 98px; width: 364px; height: 362px; background: var(--ink); }
  .front-rule-v { left: 347px; top: 98px; width: 3px; height: 334px; background: var(--paper); }
  .front-rule-h { left: 0; top: 429px; width: 350px; height: 3px; background: var(--paper); }

  /* back card brand block */
  .back-brand { left: 0; top: 0; width: 378px; height: 380px; background: var(--paper); }
  .back-gap { left: 385px; top: 0; width: 15px; height: 460px; background: var(--paper); }

  .wordmark {
    position: absolute; transform: translate(-50%, -50%);
    font-weight: 700; font-size: 40px; letter-spacing: 1px; line-height: 1;
    white-space: nowrap;
  }
  .card--front .wordmark { left: 168px; top: 264px; color: var(--paper); }
  .card--back .wordmark { left: 204px; top: 221px; color: var(--ink); }

  .person { position: absolute; line-height: 1.22; }
  .person__name { font-weight: 700; font-size: 23px; }
  .person__role, .person__phone { font-size: 20px; }
  .card--front .person { left: 613px; top: 111px; }
  .card--back .person { left: 607px; top: 62px; }

  .company { position: absolute; }
  .company__name { font-size: 30px; line-height: 1; margin-bottom: 12px; }
  .company__line { font-size: 23px; line-height: 1; height: 33px; }
  .card--front .company { left: 398px; top: 219px; }
  .card--back .company { left: 432px; top: 161px; }
</style>
</head>
<body>
<div class="canvas">

  <section class="card card--front">
    <div class="block front-brand"></div>
    <div class="block front-rule-v"></div>
    <div class="block front-rule-h"></div>
    <div class="wordmark">VELMARINE</div>
    <div class="person">
      <div class="person__name">Tiago Moreira</div>
      <div class="person__role">Manager</div>
      <div class="person__phone">+351 912480375</div>
    </div>
    <div class="company">
      <div class="company__name">Velmarine, LDA</div>
      <div class="company__line">Rua das Oliveiras, 42</div>
      <div class="company__line">1900-118 Lisboa</div>
      <div class="company__line">+351 210456789</div>
      <div class="company__line">geral@velmarine-oficina.pt</div>
      <div class="company__line">www.velmarine-oficina.pt/contactos</div>
    </div>
  </section>

  <section class="card card--back">
    <div class="block back-brand"></div>
    <div class="block back-gap"></div>
    <div class="wordmark">VELMARINE</div>
    <div class="person">
      <div class="person__name">Tiago Moreira</div>
      <div class="person__role">Manager</div>
      <div class="person__phone">+351 912480375</div>
    </div>
    <div class="company">
      <div class="company__name">Velmarine, LDA</div>
      <div class="company__line">Rua das Oliveiras, 42</div>
      <div class="company__line">1900-118 Lisboa</div>
      <div class="company__line">+351 210456789</div>
      <div class="company__line">geral@velmarine-oficina.pt</div>
      <div class="company__line">www.velmarine-oficina.pt/contactos</div>
    </div>
  </section>

</div>
</body>
</html>
```